Velvet Lantern rebranding my business with a new business card

I have my new logo and now I need a refresher on my business cards. I really want something fun and fresh. I like black background or anything to make the color pop.
Logo
Name: Velvet Lantern
Contact Info as stated below:
Mara Pelkin
519-555-0147
Logo
Name: Velvet Lantern
Mara Pelkin
519-555-0147
fb.me/VelvetLanternbyMara
Instagram: @VelvetLanternbyMara

Industry/Entity Type

Business

Contact Information for Business Card

double-sided. Logo on one side. Contact info on the other.

Requirements
Must have
• Logo
• Name: Velvet Lantern
• Contact Info as stated below:
• Mara Pelkin
• 519-555-0147
• fb.me/VelvetLanternbyMara
• fb.me/VelvetLanternbyMara

```html
<!DOCTYPE html>
<html lang="en">
<head>
<meta charset="utf-8">
<title>Velvet Lantern – Business Card</title>
<link rel="stylesheet" href="https://fonts.googleapis.com/css2?family=Lobster+Two&family=Raleway:wght@400;600&display=swap">
<style>
  :root {
    --backdrop: #0e0e0e;
    --card: #161616;
    --mint: #78c77e;
    --rose: #e07fc0;
    --cream: #efe6c8;
    --ink-soft: #d9d3c4;
  }
  * { box-sizing: border-box; margin: 0; padding: 0; }
  html, body {
    width: 1200px; height: 1000px; overflow: hidden;
    background: var(--backdrop);
  }
  .sheet {
    position: relative; width: 1200px; height: 1000px;
    display: flex; align-items: center; justify-content: center; gap: 60px;
  }
  .card {
    position: relative; width: 500px; height: 290px;
    background: var(--card); border-radius: 22px; overflow: hidden;
    box-shadow: 0 10px 30px rgba(0,0,0,0.6);
  }
  .card-rings { position: absolute; inset: 0; }
  .card-content {
    position: absolute; inset: 0;
    display: flex; flex-direction: column; align-items: center; justify-content: center;
  }
  .brand-mark {
    font-family: "Raleway", sans-serif; font-weight: 600;
    color: var(--cream); display: flex; align-items: center; gap: 8px;
  }
  .brand-mark .dot {
    width: 10px; height: 10px; border-radius: 50%; background: var(--cream);
  }
  .front .brand-mark { font-size: 14px; margin-bottom: 14px; letter-spacing: 0.5px; }
  .owner-name {
    font-family: "Lobster Two", sans-serif; font-size: 40px;
    color: var(--rose); letter-spacing: 1px; margin-bottom: 14px;
  }
  .contact-line {
    font-family: "Raleway", sans-serif; font-size: 14px;
    display: flex; align-items: center; gap: 10px; line-height: 1.6;
  }
  .phone { color: var(--ink-soft); }
  .handle { color: var(--mint); }
  .social-dot {
    width: 14px; height: 14px; border-radius: 50%; background: var(--cream);
  }
  .back .brand-mark { font-size: 34px; gap: 14px; }
  .back .brand-mark .dot { width: 22px; height: 22px; background: var(--rose); }
  .back .brand-mark { color: var(--cream); }
</style>
</head>
<body>
<main class="sheet">
  <section class="card front" aria-label="Contact side">
    <svg class="card-rings" width="500" height="290" viewBox="0 0 500 290">
      <circle cx="250" cy="145" r="182" fill="none" stroke="var(--mint)" stroke-width="5"/>
      <circle cx="250" cy="145" r="168" fill="none" stroke="var(--mint)" stroke-width="5"/>
    </svg>
    <div class="card-content">
      <div class="brand-mark"><span class="dot"></span>Velvet Lantern</div>
      <h1 class="owner-name">Mara Pelkin</h1>
      <p class="contact-line phone">519-555-0147</p>
      <p class="contact-line handle"><span class="social-dot"></span>VelvetLanternbyMara<span class="social-dot"></span></p>
    </div>
  </section>

  <section class="card back" aria-label="Logo side">
    <svg class="card-rings" width="500" height="290" viewBox="0 0 500 290">
      <circle cx="250" cy="145" r="182" fill="none" stroke="var(--rose)" stroke-width="5"/>
      <circle cx="250" cy="145" r="168" fill="none" stroke="var(--rose)" stroke-width="5"/>
    </svg>
    <div class="card-content">
      <div class="brand-mark"><span class="dot"></span>Velvet Lantern</div>
    </div>
  </section>
</main>
</body>
</html>
```